'WILD' eye catching Business Card Design / Logo for production company / TV host / adventurer

Hi there,

We are looking for a 'WILD' and exciting logo and double sided business card for our business "Red Kettle Studios".

Corwin Baxley is an international television host, adventurer, author and inspirational public speaker.

We want to project Corwin's talents onto his business card.

We are looking for a business card design that can carry over onto letter heads, emails etc. We want a design that is 'WILD', different and exciting.

Feel free to check out Corwin's web site: www.redkettlestudios.co.nz to get a better understanding what he is about.

Please feel free to go completely 'WILD' on this project as we want something different with lots of WOW factors.

Thank you so much and we look forward to your designs.

We have a feeling that there will be many more designs in the near future.

Best regards,

the production team

We have added another task to the list.

If the winning designer can also provide us with a matching letterhead and email signature based on the same style of design as the business card.

Target Market(s)

People with passion.

Industry/Entity Type

Business

Requirements
Must have
• Red Kettle Studios
Corwin Baxley
42 Fernhill Lane
Ashbury 7388
New Zealand

Phone +64-(0)3-5027 416
Cell +64-(0)274-861 052

email: redkettlenz@mailbox-example.nz
www.redkettlestuios.co.nz
Nice to have
• A feature made out of the name 'Red Kettle Studios'.

Corwin Baxley's name reasonably obvious.

All other details (except web site) can be quite small.

```html
<!DOCTYPE html>
<html lang="en">
<head>
<meta charset="utf-8">
<title>Red Kettle Studios – Business Card</title>
<link rel="stylesheet" href="https://fonts.googleapis.com/css2?family=PT+Sans:wght@400;700&display=swap">
<style>
  :root {
    --spectrum-core: #ff00c8;
    --spectrum-violet: #7a00ff;
    --spectrum-blue: #1a1aff;
    --spectrum-cyan: #00e5ff;
    --spectrum-green: #19ff3a;
    --spectrum-yellow: #fff200;
    --spectrum-orange: #ff7a00;
    --spectrum-red: #ff0000;
    --ink-black: #000000;
    --ink-address: #ff1f3d;
    --ink-tagline: #2f4a00;
    --name-top: #19d0ff;
    --name-bottom: #1858c8;
    --cell-top: #7a48c8;
    --cell-bottom: #5a5a7a;
    --web-top: #b4ff2a;
    --web-bottom: #1f8a2a;
  }
  html, body {
    margin: 0;
    padding: 0;
    width: 1200px;
    height: 686px;
    overflow: hidden;
    background: #ffffff;
  }
  .business-card {
    position: relative;
    width: 1200px;
    height: 686px;
    overflow: hidden;
    font-family: "PT Sans", Arial, sans-serif;
    background: radial-gradient(circle at 340px 230px,
      var(--spectrum-core) 0px,
      var(--spectrum-violet) 80px,
      var(--spectrum-blue) 140px,
      var(--spectrum-cyan) 230px,
      var(--spectrum-green) 320px,
      var(--spectrum-yellow) 410px,
      var(--spectrum-orange) 490px,
      var(--spectrum-red) 570px);
  }
  .brand-name {
    position: absolute;
    left: 34px;
    top: 188px;
    margin: 0;
    font-size: 54px;
    font-weight: 700;
    color: var(--ink-black);
    letter-spacing: 1px;
    white-space: nowrap;
  }
  .host-block {
    position: absolute;
    left: 743px;
    top: 118px;
    white-space: nowrap;
  }
  .host-name {
    margin: 0;
    font-size: 66px;
    font-weight: 700;
    line-height: 1;
    background: linear-gradient(180deg, var(--name-top), var(--name-bottom));
    -webkit-background-clip: text;
    background-clip: text;
    color: transparent;
  }
  .host-roles {
    margin: 6px 0 0 18px;
    font-size: 22px;
    font-weight: 700;
    line-height: 1.6;
    color: var(--ink-tagline);
  }
  .host-cell {
    margin: 6px 0 0 0;
    font-size: 34px;
    font-weight: 700;
    background: linear-gradient(180deg, var(--cell-top), var(--cell-bottom));
    -webkit-background-clip: text;
    background-clip: text;
    color: transparent;
  }
  .contact-block {
    position: absolute;
    left: 190px;
    top: 418px;
    font-style: normal;
    font-size: 27px;
    font-weight: 700;
    line-height: 39px;
    color: var(--ink-address);
    white-space: nowrap;
  }
  .contact-email {
    color: var(--ink-address);
    -webkit-text-stroke: 1px var(--ink-black);
  }
  .website {
    position: absolute;
    left: 190px;
    top: 620px;
    margin: 0;
    font-size: 50px;
    font-weight: 400;
    line-height: 1;
    white-space: nowrap;
    background: linear-gradient(180deg, var(--web-top), var(--web-bottom));
    -webkit-background-clip: text;
    background-clip: text;
    color: transparent;
  }
</style>
</head>
<body>
  <main class="business-card">
    <h1 class="brand-name">RED KETTLE STUDIOS</h1>

    <section class="host-block">
      <h2 class="host-name">Corwin Baxley</h2>
      <p class="host-roles">Television host, adventurer, author<br>and inspirational public speaker</p>
      <p class="host-cell">cell:64-(0)274-861 052</p>
    </section>

    <address class="contact-block">
      42 Fernhill Lane<br>
      Ashbury 7388<br>
      New Zealand<br>
      Phone : 64-(0)3-5027 416<br>
      <span class="contact-email">email: redkettlenz@mailbox-example.nz</span>
    </address>

    <p class="website">www.redkettlestudios.co.nz</p>
  </main>
</body>
</html>
```